Carte d'affaire bilingue

Nous avons besoin d'une carte d'affaire pour notre entreprise spécialisée en vente et achat de terrain. Nous sommes une agence immobilière et nous voulons une carte avec le recto en Français et le verso en anglais. Nous voulons une image sobre et épurée. Nous avons de la clientèle internationale et nous voulons une carte très professionnelle mais qui se démarque. Nous voulons cibler une clientèle commerciale, industrielle, contracteurs et promoteurs immobiliers.
Updates

Hi everybody, we saw all your conception and we are approching of what we like but the "WOW" is missing.

We love the little sign to specify (phone or email) but we can put them in a square to make like our logo, we love also dark gray not lite gray, we also love the stainless lines. In our logo you can see a little sign +. For us is signyfy " Always further" so if you can put many little +++++ in the conception somewhere very discret it will be appreciate. We also like a kind of round that make a magnyfying glass, because we search land we found opportunity.

Thank you

Reason: I ask different things in the last day but no one do what i am asking for. For the conception # 3016702 that we love we ask changes.

We like simplicity, urban design, corporate, international. The card must have one side in french and the other side in english. We like dark gray,silver, and a little bit of green.

Target Market(s)

Investors, developers, construction builders, etc...

Font styles to use
Serif
Sans Serif

Requirements
Must have
• logo
La mention: Agence immobilière (Francais) / Real Estate Agency (anglais)
Sous le nom: Courtier immobilier agréé (Français) / Real Estate Broker

```html
<!DOCTYPE html>
<html lang="fr">
<head>
<meta charset="utf-8">
<title>Carte d'affaire bilingue</title>
<link href="https://fonts.googleapis.com/css2?family=Cinzel:wght@400;600;700&display=swap" rel="stylesheet">
<style>
  :root {
    --ink: #141818;
    --logo-ink: #3a4244;
    --green: #2f9a1c;
    --divider: #25292a;
    --steel: #a8b0b0;
  }
  * { margin: 0; padding: 0; box-sizing: border-box; }
  html, body {
    width: 1009px; height: 1200px; overflow: hidden;
    background: var(--divider);
    font-family: "Cinzel", serif;
    color: var(--ink);
  }
  .sheet { position: relative; width: 1009px; height: 1200px; }
  .card {
    position: absolute; left: 0; width: 1009px; height: 591px; overflow: hidden;
  }
  .card--fr { top: 0; height: 590px; }
  .card--en { top: 609px; }
  .card__backdrop { position: absolute; inset: 0; width: 100%; height: 100%; }
  .brand { position: absolute; left: 47px; top: 51px; width: 546px; height: 122px; }
  .brand__square {
    position: absolute; left: 0; top: 0; width: 110px; height: 110px;
    background: var(--green);
  }
  .brand__name {
    position: absolute; left: 138px; top: 0;
    font-size: 50px; font-weight: 400; line-height: 56px; color: var(--logo-ink);
  }
  .brand__rule {
    position: absolute; left: 0; top: 120px; width: 546px; height: 2px; background: var(--steel);
  }
  .agency {
    position: absolute; right: 418px; top: 182px;
    font-size: 21px; font-weight: 600; letter-spacing: 0.5px;
  }
  .person { position: absolute; left: 50px; top: 280px; }
  .person__name { font-size: 52px; font-weight: 700; line-height: 58px; letter-spacing: 2px; }
  .person__title { font-size: 22px; font-weight: 600; line-height: 30px; }
  .web {
    position: absolute; right: 59px; top: 326px; text-align: right;
    font-size: 21px; font-weight: 600; line-height: 23px;
  }
  .contact {
    position: absolute; left: 0; width: 100%; text-align: center;
    font-size: 23px; font-weight: 600; letter-spacing: 1.5px;
  }
  .contact--phones { top: 462px; word-spacing: 3px; }
  .contact--address { top: 506px; font-size: 23px; letter-spacing: 4px; }
</style>
</head>
<body>
<div class="sheet">

  <section class="card card--fr" lang="fr">
    <svg class="card__backdrop" viewBox="0 0 1009 590" preserveAspectRatio="none" aria-hidden="true">
      <defs>
        <linearGradient id="shade-fr" x1="0" y1="0" x2="0" y2="1">
          <stop offset="0" stop-color="#f6f7f7"/>
          <stop offset="0.45" stop-color="#a9b1b1"/>
          <stop offset="0.8" stop-color="#cdd2d2"/>
        </linearGradient>
        <linearGradient id="sheen-fr" x1="0" y1="0" x2="1" y2="0">
          <stop offset="0" stop-color="#d6dada"/>
          <stop offset="1" stop-color="#e8eaea"/>
        </linearGradient>
      </defs>
      <rect width="1009" height="590" fill="url(#shade-fr)"/>
      <path d="M0,470 C300,470 520,420 700,300 C820,220 910,165 1009,135 L1009,590 L0,590 Z" fill="url(#sheen-fr)"/>
      <path d="M0,470 C300,470 520,420 700,300 C820,220 910,165 1009,135" fill="none" stroke="#f4f5f5" stroke-width="2" opacity="0.7"/>
    </svg>

    <div class="brand">
      <span class="brand__square"></span>
      <div class="brand__name">Le Repère<br>Foncier</div>
      <span class="brand__rule"></span>
    </div>
    <div class="agency">Agence immobilière</div>

    <div class="person">
      <div class="person__name">Sylvie Marchand</div>
      <div class="person__title">Courtier immobilier agréé, D.A.</div>
      <div class="person__title">Vice-Présidente</div>
    </div>
    <div class="web">s.marchand@lrfx.com<br>www.lrfx.com</div>

    <div class="contact contact--phones">T. 514 555 0142 &nbsp;F. 450 555 0187 &nbsp;C. 514 555 0163 &nbsp;SF 1 866 555 0100</div>
    <div class="contact contact--address">12 B, rue des Artisans, 2e, Laval, Qc, H7L 0A1</div>
  </section>

  <section class="card card--en" lang="en">
    <svg class="card__backdrop" viewBox="0 0 1009 591" preserveAspectRatio="none" aria-hidden="true">
      <defs>
        <linearGradient id="shade-en" x1="0" y1="0" x2="0" y2="1">
          <stop offset="0" stop-color="#f6f7f7"/>
          <stop offset="0.45" stop-color="#a9b1b1"/>
          <stop offset="0.8" stop-color="#cdd2d2"/>
        </linearGradient>
        <linearGradient id="sheen-en" x1="0" y1="0" x2="1" y2="0">
          <stop offset="0" stop-color="#d6dada"/>
          <stop offset="1" stop-color="#e8eaea"/>
        </linearGradient>
      </defs>
      <rect width="1009" height="591" fill="url(#shade-en)"/>
      <path d="M0,475 C300,475 520,425 700,305 C820,225 910,170 1009,140 L1009,591 L0,591 Z" fill="url(#sheen-en)"/>
      <path d="M0,475 C300,475 520,425 700,305 C820,225 910,170 1009,140" fill="none" stroke="#f4f5f5" stroke-width="2" opacity="0.7"/>
    </svg>

    <div class="brand">
      <span class="brand__square"></span>
      <div class="brand__name">Parcel<br>Point</div>
      <span class="brand__rule"></span>
    </div>
    <div class="agency">Real estate Agency</div>

    <div class="person">
      <div class="person__name">Sylvie Marchand</div>
      <div class="person__title">Real estate broker, D.A.</div>
      <div class="person__title">Vice-President</div>
    </div>
    <div class="web">s.marchand@lrfx.com<br>www.lrfx.com</div>

    <div class="contact contact--phones">P. 514 555 0142 &nbsp;F. 450 555 0187 &nbsp;C. 514 555 0163 &nbsp;TF 1 866 555 0199</div>
    <div class="contact contact--address">12 B, Artisans St., 2e, Laval, Qc, H7L 0A1</div>
  </section>

</div>
</body>
</html>
```